Brovanix Stationery Design Project

We need a stationery design for our new business Brovanix which deals in advanced cleaning technologies such as Ultrasonic cleaning and high pressure cleaning machinery.

Our colour scheme is as per the included files.

We require business cards, letterheads, a brochure folder and email signatures design
Updates

Apologies for the delay in making a decision on this project. We will be making a final decision during the course of next week

Target Market(s)

Industries ranging from medical, automotive, mining, engineering all requiring specialised cleaning services

Industry/Entity Type

Pressure Cleaning

Requirements
Must have
• Please include our supplied logo and colour scheme. The design needs to be professional but creative.

```html
<!DOCTYPE html>
<html lang="en">
<head>
<meta charset="utf-8">
<title>Brovanix Letterhead</title>
<link href="https://fonts.googleapis.com/css2?family=Source+Sans+3:wght@400;600;700&display=swap" rel="stylesheet">
<style>
  :root {
    --paper: #ffffff;
    --brand-grey: #8a8b8d;
    --grey-tab: #7b7c7e;
    --blue-deep: #233f8c;
    --blue-light: #3e6bbd;
    --watermark: #e6eaf2;
    --ink-light: #ffffff;
  }
  * { margin: 0; padding: 0; box-sizing: border-box; }
  html, body {
    width: 928px;
    height: 1200px;
    overflow: hidden;
    background: var(--paper);
    font-family: "Source Sans 3", "Helvetica Neue", Arial, sans-serif;
  }
  .letterhead {
    position: relative;
    width: 928px;
    height: 1200px;
    background: var(--paper);
  }
  .brand {
    position: absolute;
    left: 45px;
    top: 52px;
    color: var(--brand-grey);
  }
  .brand-name {
    display: flex;
    align-items: center;
    gap: 14px;
    font-weight: 700;
    font-size: 42px;
    line-height: 1;
    letter-spacing: 1px;
  }
  .brand-mark {
    width: 38px;
    height: 38px;
    background: var(--blue-deep);
  }
  .brand-tagline {
    margin-top: 4px;
    margin-left: 52px;
    font-size: 16px;
    font-weight: 400;
  }
  .contact-band {
    position: absolute;
    left: 558px;
    top: 53px;
    width: 298px;
    height: 132px;
  }
  .contact-list {
    position: absolute;
    right: 20px;
    top: 10px;
    list-style: none;
    text-align: right;
    color: var(--ink-light);
    font-size: 14.5px;
    font-weight: 600;
    letter-spacing: 0.8px;
    line-height: 21.5px;
  }
  .contact-list .address { margin-bottom: 6px; }
  .side-tab {
    position: absolute;
    left: 870px;
    top: 53px;
    width: 58px;
    height: 132px;
    background: var(--grey-tab);
  }
  .watermark {
    position: absolute;
    left: 0;
    top: 810px;
    width: 520px;
    height: 390px;
    background: var(--watermark);
  }
</style>
</head>
<body>
  <main class="letterhead">
    <header>
      <div class="brand">
        <div class="brand-name"><span class="brand-mark"></span>BROVANIX</div>
        <div class="brand-tagline">Advanced Cleaning Technologies</div>
      </div>

      <div class="contact-band">
        <svg width="298" height="132" viewBox="0 0 298 132" aria-hidden="true">
          <defs>
            <linearGradient id="bandFill" x1="0" y1="1" x2="1" y2="0">
              <stop offset="0" stop-color="var(--blue-light)"/>
              <stop offset="1" stop-color="var(--blue-deep)"/>
            </linearGradient>
          </defs>
          <polygon points="62,0 298,0 298,132 0,132" fill="url(#bandFill)"/>
        </svg>
        <ul class="contact-list">
          <li class="address">Address: your address here</li>
          <li>Phone: 000-000-0000</li>
          <li>Fax: 000-000-0000</li>
          <li>Website: brovanix.com</li>
          <li>Email: info@brovanix.com</li>
        </ul>
      </div>
      <div class="side-tab"></div>
    </header>

    <div class="watermark" role="img" aria-label="Faint brand watermark area"></div>
  </main>
</body>
</html>
```